Tumble Nest - mobile play centre poster designs

Who are we - we are a mobile playground business that specialises in providing entertainment to children in a safe, clean environment either at home or in a function centre. Brief - create 4 different signs to be displayed on our playgrounds. Please find attached 3 photos from our competitors to use as a guide. Corflute sign - size A1 Toddler zone - size A1 Playground rules - size A4 No climbing - size 20cmx8cm sending through photos and documents now.
Colors
Designer to choose colors to be used in the design.
Requirements
Must have
- Colour, be very specific with the rules, pictures

```html
<!DOCTYPE html>
<html lang="en">
<head>
<meta charset="utf-8">
<title>Tumble Nest – Toddler Zone Signs</title>
<link rel="stylesheet" href="https://fonts.googleapis.com/css2?family=Ubuntu:wght@500;700&family=Anton&family=Open+Sans:wght@400&display=swap">
<style>
  :root {
    --backdrop: #e4e4e2;
    --yellow: #f5d50f;
    --yellow-light: #fbe64a;
    --frame-green: #3f8f2a;
    --panel-top: #fbfbe6;
    --panel-mid: #fffbe4;
    --panel-mint: #e9f4ec;
    --ink-green: #13612b;
    --title-green: #7dbd3a;
    --logo-grey: #5e5e5e;
    --plant-dark: #1e5e1c;
    --plant-mid: #4f9a2c;
    --label: #222;
  }
  * { box-sizing: border-box; margin: 0; padding: 0; }
  html, body { width: 1200px; height: 897px; overflow: hidden; }
  body {
    background: var(--backdrop);
    position: relative;
    font-family: "Ubuntu", "Open Sans", sans-serif;
  }
  .sheet-label {
    position: absolute;
    top: 64px;
    font-family: "Open Sans", sans-serif;
    font-size: 16px;
    color: var(--label);
  }
  .poster {
    position: absolute;
    top: 104px;
    width: 510px;
    height: 720px;
    background: repeating-linear-gradient(180deg, var(--yellow) 0 26px, var(--yellow-light) 26px 52px);
    box-shadow: 0 6px 14px rgba(0,0,0,.28);
  }
  .poster--zone { left: 72px; }
  .poster--notice { left: 636px; }
  .poster__panel {
    position: absolute;
    left: 34px; right: 34px; top: 28px; bottom: 24px;
    background:
      radial-gradient(ellipse at 85% 70%, var(--panel-mint) 0%, transparent 55%),
      radial-gradient(ellipse at 10% 30%, #eef3d6 0%, transparent 45%),
      linear-gradient(180deg, var(--panel-top), var(--panel-mid));
    text-align: center;
    color: var(--ink-green);
    overflow: hidden;
  }
  .poster__frame {
    position: absolute;
    left: 28px; right: 28px; top: 22px; bottom: 22px;
    border: 7px solid var(--frame-green);
    pointer-events: none;
  }
  .brand {
    position: absolute;
    top: 76px; left: 0; right: 0;
    display: flex; align-items: center; justify-content: center; gap: 12px;
  }
  .brand__mark {
    width: 22px; height: 22px; border-radius: 50%;
    background: var(--title-green);
  }
  .brand__name {
    font-family: "Ubuntu", sans-serif;
    font-weight: 700;
    font-size: 50px;
    color: var(--ink-green);
    letter-spacing: 1px;
  }
  .brand__sub {
    position: absolute;
    top: 140px; left: 0; right: 0;
    font-weight: 500;
    font-size: 26px;
    color: var(--logo-grey);
    letter-spacing: 1px;
  }
  .zone-title {
    position: absolute;
    top: 196px; left: 0; right: 0;
    font-family: "Anton", sans-serif;
    font-weight: 400;
    font-size: 56px;
    letter-spacing: 3px;
    color: var(--title-green);
    text-shadow: 2px 3px 2px rgba(0,0,0,.35);
  }
  .zone-rules {
    position: absolute;
    top: 318px; left: 0; right: 0;
    font-weight: 700;
    font-size: 24px;
    line-height: 32px;
  }
  .zone-rules p + p { margin-top: 32px; }
  .notice-text {
    position: absolute;
    top: 222px; left: 6px; right: 6px;
    font-weight: 700;
    font-size: 19.5px;
    line-height: 25.6px;
  }
  .notice-text p + p { margin-top: 25.6px; }
  .notice-text .thanks { margin-top: 46px; }
  .foliage {
    position: absolute;
    left: 0; right: 0; bottom: 0;
    height: 76px;
    background:
      radial-gradient(ellipse at 20% 100%, var(--plant-dark) 0 40%, transparent 60%),
      radial-gradient(ellipse at 65% 100%, var(--plant-dark) 0 38%, transparent 60%),
      linear-gradient(180deg, transparent 0%, var(--plant-mid) 45%, var(--plant-dark) 100%);
  }
</style>
</head>
<body>

  <div class="sheet-label" style="left:96px">Toddler zone</div>
  <div class="sheet-label" style="left:636px">Toddler zone</div>

  <section class="poster poster--zone">
    <div class="poster__panel">
      <div class="brand"><span class="brand__mark"></span><span class="brand__name">Tumble Nest</span></div>
      <div class="brand__sub">MOBILE PLAY CENTRE</div>
      <h1 class="zone-title">TODDLER ZONE</h1>
      <div class="zone-rules">
        <p>0-3 yearolds ONLY<br>Supervision required at all times</p>
        <p>Parents please wear socks too</p>
      </div>
      <div class="foliage" role="img" aria-label="Jungle foliage illustration along the bottom edge"></div>
    </div>
    <div class="poster__frame"></div>
  </section>

  <section class="poster poster--notice">
    <div class="poster__panel">
      <div class="brand"><span class="brand__mark"></span><span class="brand__name">Tumble Nest</span></div>
      <div class="brand__sub">MOBILE PLAY CENTRE</div>
      <div class="notice-text">
        <p>If using the toddler soft play equipment,<br>please ensure that this area is used by<br>children 0-3 ONLY.</p>
        <p>The equipment and ball pit is only<br>designed for small children and bigger<br>kids might injure themselves, the<br>smaller children or cause extensive<br>damage to the equipment, of which<br>there will be a charge back to the client.</p>
        <p class="thanks">Thank you</p>
      </div>
      <div class="foliage" role="img" aria-label="Jungle foliage illustration along the bottom edge"></div>
    </div>
    <div class="poster__frame"></div>
  </section>

</body>
</html>
```